Covid19 Poster for workplaces

Create a poster on how to protect yourself from Corona virus at work.
We are a Kindred Works company. We have just re-branded so we need to fit in with our brand. We like clean and fresh, slightly amusing is ok if it will draw attention but it's an important topic. A4 and A3 please.

Content:

Headline: Lower the risk of COVID 19 in the workplace.

BE WELL

Bring your own cup - don’t share cups and food.
Elbow tap instead of handshakes and kisses
Wash your hands often - with soap.
Elbow or tissues when you cough or sneeze then straight in the bin
Leave your face alone after touching shared surfaces
Leave your bugs at home if you’re feeling unwell.

Call health line if you have a cough, a high temperature and shortness of breath. 0800 472 9160

Based on recommendations from ZPK and QLN

Target Market(s)

Employees - so anyone

Other font styles liked:
• Use the closest font to the brand documents

Requirements
Should not have
• Clip art

```html
<!DOCTYPE html>
<html lang="en">
<head>
<meta charset="utf-8">
<title>Lower the risk of COVID 19 in the workplace</title>
<link href="https://fonts.googleapis.com/css2?family=Open+Sans:wght@400;700;800&family=Roboto:wght@500&display=swap" rel="stylesheet">
<style>
  :root{
    --teal:#1eacb9;
    --teal-text:#1ea8b4;
    --lime:#8dc63f;
    --sun:#ffd200;
    --navy:#2d3a8c;
    --ink:#231f20;
    --deep:#0b3a52;
    --paper:#ffffff;
  }
  *{margin:0;padding:0;box-sizing:border-box}
  html,body{width:849px;height:1200px;overflow:hidden;background:var(--paper)}
  .poster{position:relative;width:849px;height:1200px;background:var(--paper);font-family:"Open Sans",sans-serif}

  .masthead{position:absolute;left:0;top:0;width:849px;height:246px;background:var(--teal)}
  .masthead-rule{position:absolute;left:0;top:246px;width:849px;height:9px;background:var(--lime)}

  .brand{position:absolute;left:56px;top:44px;display:flex;align-items:center;gap:12px}
  .brand-dot{width:22px;height:22px;background:var(--paper);border-radius:50%}
  .brand-name{font-family:"Open Sans",sans-serif;font-weight:700;font-size:31px;line-height:30px;color:var(--ink);letter-spacing:-0.5px}

  .headline{position:absolute;left:40px;top:146px;width:450px;text-align:center;color:var(--paper);font-weight:800;font-size:30px;line-height:37px}

  .hero{position:absolute;left:470px;top:29px;width:322px;height:170px;border-radius:85px;
    background:radial-gradient(circle at 70% 40%,#2f6e88 0%,var(--deep) 55%,#072a3c 100%)}
  .hero-title{position:absolute;left:470px;top:70px;width:322px;text-align:center;color:var(--paper);font-weight:800;font-size:47px;line-height:56px;letter-spacing:0.5px}

  .tips{position:absolute;left:0;top:270px;width:849px;list-style:none}
  .tip{position:absolute;left:0;width:849px;display:flex;align-items:center}
  .tip-icon{position:absolute;left:70px;width:88px;height:80px;display:flex;align-items:center;justify-content:center}
  .tip-icon .glyph{width:70px;height:70px;border-radius:14px;background:var(--teal-text)}
  .tip-text{position:absolute;left:178px;width:560px;font-family:"Roboto",sans-serif;font-weight:500;font-size:23px;line-height:32px;color:var(--teal-text)}

  .sun-rule{position:absolute;left:0;top:923px;width:849px;height:10px;background:var(--sun)}
  .helpline{position:absolute;left:0;top:933px;width:849px;height:108px;background:var(--navy)}
  .helpline-number{position:absolute;left:68px;top:24px;font-weight:800;font-size:52px;line-height:60px;color:var(--sun);letter-spacing:-0.5px}
  .helpline-note{position:absolute;left:430px;top:10px;width:362px;text-align:center;color:var(--paper);font-size:23px;line-height:29px}
  .helpline-note strong{font-weight:800}

  .sources{position:absolute;left:0;top:1062px;width:849px;text-align:center;color:var(--navy);font-weight:800;font-size:23px;line-height:32px;letter-spacing:0.3px}
  .partners{position:absolute;left:0;top:1105px;width:849px;display:flex;justify-content:center;gap:90px;align-items:center}
  .partner{display:flex;align-items:center;gap:10px;font-weight:700;font-size:34px;color:var(--navy)}
  .partner-mark{width:30px;height:30px;background:var(--navy);border-radius:50%}
  .partner-mark.square{border-radius:0}
</style>
</head>
<body>
<main class="poster">
  <header>
    <div class="masthead"></div>
    <div class="brand">
      <span class="brand-dot"></span>
      <span class="brand-name">Kindred<br>Works</span>
    </div>
    <h1 class="headline">Lower the risk of COVID 19 in the workplace</h1>
    <div class="hero" role="img" aria-label="Dark teal close-up imagery of virus particles"></div>
    <p class="hero-title">BE WELL</p>
    <div class="masthead-rule"></div>
  </header>

  <ul class="tips">
    <li class="tip" style="top:22px">
      <span class="tip-icon">
        <svg width="76" height="80" viewBox="0 0 76 80" aria-hidden="true">
          <g fill="none" stroke="var(--teal-text)" stroke-width="2.5" stroke-linecap="round">
            <path d="M25 4c-4 4 4 7 0 11M33 4c-4 4 4 7 0 11M41 4c-4 4 4 7 0 11"/>
          </g>
          <path d="M13 26h48v8h4a11 11 0 0 1 0 22h-7c-4 8-10 10-19 10h-8C17 66 13 56 13 42z" fill="var(--teal-text)"/>
          <path d="M61 38h3a6 6 0 0 1 0 12h-5z" fill="var(--paper)"/>
          <path d="M2 70h72c-2 5-5 7-10 7H12c-5 0-8-2-10-7z" fill="var(--teal-text)"/>
        </svg>
      </span>
      <span class="tip-text">Bring your own cup - don’t share cups and food.</span>
    </li>
    <li class="tip" style="top:119px">
      <span class="tip-icon"><span class="glyph" role="img" aria-label="Icon of two elbows tapping"></span></span>
      <span class="tip-text">Elbow tap instead of handshakes and kisses.</span>
    </li>
    <li class="tip" style="top:216px">
      <span class="tip-icon"><span class="glyph" role="img" aria-label="Icon of hands being washed under water"></span></span>
      <span class="tip-text">Wash your hands often - with soap.</span>
    </li>
    <li class="tip" style="top:313px">
      <span class="tip-icon" style="height:96px"><span class="glyph" style="height:80px" role="img" aria-label="Icon of a person sneezing"></span></span>
      <span class="tip-text">Elbow or tissues when you cough or sneeze, then straight in the bin.</span>
    </li>
    <li class="tip" style="top:442px">
      <span class="tip-icon" style="height:96px"><span class="glyph" style="height:80px;width:56px" role="img" aria-label="Icon of a finger touching a surface"></span></span>
      <span class="tip-text">Leave your face alone after touching shared surfaces.</span>
    </li>
    <li class="tip" style="top:586px">
      <span class="tip-icon">
        <svg width="80" height="76" viewBox="0 0 80 76" aria-hidden="true">
          <path d="M12 4h6v12z" fill="var(--teal-text)"/>
          <path d="M2 36 40 2l38 34-4 4L40 10 6 40z" fill="var(--teal-text)"/>
          <path d="M13 36 40 13l27 23v38H47V55H33v19H13z" fill="var(--teal-text)"/>
        </svg>
      </span>
      <span class="tip-text">Leave your bugs at home if you’re feeling unwell.</span>
    </li>
  </ul>

  <footer>
    <div class="sun-rule"></div>
    <section class="helpline">
      <p class="helpline-number">0800 472 9160</p>
      <p class="helpline-note"><strong>CALL HEALTH LINE</strong> if you have a cough, a high temperature and shortness of breath</p>
    </section>
    <p class="sources">BASED ON RECOMMENDATIONS FROM</p>
    <div class="partners">
      <span class="partner"><span class="partner-mark"></span>ZPK</span>
      <span class="partner"><span class="partner-mark square"></span>QLN</span>
    </div>
  </footer>
</main>
</body>
</html>
```